Talent Management Company Needs Business Cards

Using one of the logos provided (attached) K&R Talent Collective needs a business card designed.
Please visit our website for more information about us-

www.krtalentcollective.example

The face should feature a dramatic presentation of the logo with the back being reserved for our professional information which is:

The information should be:
Dorian T. Vickers
C.E.O
Email: dtvickers@krtalentcollective.example
Mobile: 555-804-2917
Website: www.krtalentcollective.example

Marcus L. Vickers
Director of Public Relations
Email: mlvickers@krtalentcollective.example
Mobile: 555-806-3350

Jules R. Hampton
Director of Client Development
Email: jhampton@krtalentcollective.example

Simon Hurlock
Director of Brand Development
Email: shurlock@krtalentcollective.example

Would like the logo to have color. I would like to see one side red or black and the other side white but if it looks better in either black or red that would be fine to but would like to see how it comes out.

Please feel free to message me and if you would like just the icon alone I have other image files that I can send as well.

Target Market(s)

Professional Athletes, coaches, entertainers age 18-35 but also must be accepted in the business community

Industry/Entity Type

Business

Requirements
Must have
• 1) Use the logo
2) Double sided
3) Distinctive
Nice to have
• Small simple images for telephone, e-mail, and Url.

```html
<!DOCTYPE html>
<html lang="en">
<head>
<meta charset="utf-8">
<title>K&amp;R Talent Collective — Business Card</title>
<link rel="stylesheet" href="https://fonts.googleapis.com/css2?family=Open+Sans:ital,wght@0,400;0,700;1,400&display=swap">
<style>
  :root {
    --stage: #e9e6e2;
    --card-black: #0a0a0a;
    --brand-red: #d71920;
    --red-deep: #9c1016;
    --red-mid: #c4161d;
    --white: #ffffff;
    --silver-light: #f4f4f4;
    --silver-dark: #9a9a9a;
    --text-light: #f2f2f2;
    --shadow: rgba(0,0,0,0.35);
  }
  * { margin: 0; padding: 0; box-sizing: border-box; }
  html, body {
    width: 1200px; height: 402px; overflow: hidden;
    background: var(--stage);
    font-family: "Open Sans", Arial, sans-serif;
  }
  .canvas { position: relative; width: 1200px; height: 402px; }

  .card {
    position: absolute; width: 512px; height: 290px;
    box-shadow: 0 3px 10px var(--shadow);
    overflow: hidden;
  }
  .card--back { left: 63px; top: 56px; background: var(--card-black); }
  .card--front {
    left: 625px; top: 56px;
    background: radial-gradient(ellipse at 50% 40%, var(--red-mid) 0%, #b3141a 55%, var(--red-deep) 100%);
  }

  /* Brand wordmark */
  .wordmark {
    position: absolute; left: 0; right: 0;
    display: flex; align-items: center; justify-content: center; gap: 10px;
    color: var(--white); font-weight: 400; text-transform: uppercase;
    letter-spacing: 0.04em; white-space: nowrap;
  }
  .wordmark__square { display: block; background: var(--brand-red); }
  .card--back .wordmark { top: 104px; font-size: 17px; }
  .card--back .wordmark__square { width: 12px; height: 12px; }
  .card--front .wordmark { top: 196px; font-size: 27px; gap: 14px; }
  .card--front .wordmark__square { width: 20px; height: 20px; background: var(--white); }

  /* Name band */
  .name-band__silver {
    position: absolute; left: 0; top: 149px; width: 54px; height: 28px;
    background: linear-gradient(90deg, var(--silver-light), var(--silver-dark));
  }
  .name-band {
    position: absolute; left: 58px; right: 0; top: 149px; height: 28px;
    background: linear-gradient(90deg, var(--red-deep) 0%, var(--brand-red) 18%, var(--brand-red) 100%);
    display: flex; align-items: center; justify-content: center;
    padding-right: 60px;
    color: var(--white);
  }
  .name-band__name { font-weight: 700; font-size: 15px; }
  .name-band__title { font-style: italic; font-size: 12px; margin-left: 4px; }

  /* Contact block */
  .address {
    position: absolute; right: 300px; top: 200px;
    text-align: right; color: var(--text-light);
    font-size: 12.5px; line-height: 18px;
  }
  .contacts {
    position: absolute; left: 222px; top: 200px;
    list-style: none; color: var(--text-light);
    font-size: 12.5px; line-height: 18px;
  }
  .contacts li { display: flex; align-items: center; gap: 6px; height: 18px; }
  .contacts svg { width: 10px; height: 10px; flex: none; }
</style>
</head>
<body>
<main class="canvas">

  <section class="card card--back" aria-label="Card back with contact details">
    <div class="wordmark"><span class="wordmark__square"></span><span>K&amp;R Talent Collective</span></div>

    <div class="name-band__silver"></div>
    <div class="name-band">
      <span class="name-band__name">Dorian T. Vickers,</span>
      <span class="name-band__title">C.E.O</span>
    </div>

    <address class="address" style="font-style:normal">
      1180 Larkspur Ridge Rd<br>
      Suite 310<br>
      Fairhaven, OH 45099
    </address>

    <ul class="contacts">
      <li>
        <svg viewBox="0 0 10 10" aria-hidden="true"><rect x="2" y="0" width="6" height="10" rx="1.2" fill="var(--brand-red)"/><rect x="3.2" y="1.3" width="3.6" height="6" fill="var(--card-black)"/></svg>
        <span>555-804-2917</span>
      </li>
      <li>
        <svg viewBox="0 0 10 10" aria-hidden="true"><circle cx="5" cy="5" r="5" fill="var(--brand-red)"/><rect x="2.2" y="3.2" width="5.6" height="3.8" fill="none" stroke="var(--white)" stroke-width="0.8"/><path d="M2.2 3.2 L5 5.4 L7.8 3.2" fill="none" stroke="var(--white)" stroke-width="0.8"/></svg>
        <span>dtvickers@krtalentcollective.example</span>
      </li>
      <li>
        <svg viewBox="0 0 10 10" aria-hidden="true"><circle cx="5" cy="5" r="5" fill="var(--brand-red)"/><ellipse cx="5" cy="5" rx="2" ry="4" fill="none" stroke="var(--white)" stroke-width="0.7"/><path d="M1 5 H9 M1.8 3 H8.2 M1.8 7 H8.2" stroke="var(--white)" stroke-width="0.7"/></svg>
        <span>www.krtalentcollective.example</span>
      </li>
    </ul>
  </section>

  <section class="card card--front" aria-label="Card front with brand name">
    <div class="wordmark"><span class="wordmark__square"></span><span>K&amp;R Talent Collective</span></div>
  </section>

</main>
</body>
</html>
```